Broschüre für Gebäudereinigungsservice
Zielgruppe
Wir sind ein Gebäudeservice Unterehmen. Wir sind spezialisiert auf: Reinigungen aller Art, Grünflächenpflege aller Art, Winterdienst und Handwerkerservice aller Art. Usere Zielgruppe: Hausverwaltungen, Genossenschaften und Privatpersonen.
Aufgabenstellung
Die Broschüre soll an diese Kunden per Mail als auch ausgedruckt versendet werden.
Kunden sollen mit dieser Broschüre davon überzeugt werden uns als Gebäudeservice-Unternehmen zu beauftragen.
Unser Firmenslogan lautet 'QUALITÄT DURCH LEISTUNG.'
Die Bilder im Anhang können übernommen werden. Müssen aber nicht, bin für besserer Vorschläge gerne zu haben.
Alle Formate sind erlaubt
Bei Fragen bitte kontaktieren.
Danke!

```html
<!DOCTYPE html>
<html lang="de">
<head>
<meta charset="utf-8">
<title>Dienstleistungsübersicht – Gebäudeservice</title>
<link rel="stylesheet" href="https://fonts.googleapis.com/css2?family=Noto+Sans:wght@400;700&display=swap">
<style>
  :root {
    --teal: #3a8d8c;
    --ink: #111416;
    --divider: #2c4f55;
    --frame: #2e3032;
    --shadow: rgba(20, 60, 60, 0.55);
  }
  html, body {
    margin: 0;
    padding: 0;
    width: 1200px;
    height: 849px;
    overflow: hidden;
    background: var(--teal);
  }
  .sheet {
    position: relative;
    width: 1200px;
    height: 849px;
    background: var(--teal);
    font-family: "Noto Sans", "DejaVu Sans", sans-serif;
    color: var(--ink);
  }
  .divider {
    position: absolute;
    left: 597px;
    top: 41px;
    width: 1.5px;
    height: 766px;
    background: var(--divider);
  }
  .overview-title {
    position: absolute;
    left: 134px;
    width: 360px;
    top: 63px;
    margin: 0;
    text-align: center;
    font-size: 16px;
    font-weight: 700;
    text-decoration: underline;
  }
  .service-heading {
    position: absolute;
    margin: 0;
    font-size: 16px;
    font-weight: 700;
    text-decoration: underline;
    white-space: nowrap;
    line-height: 22px;
  }
  .service-list {
    position: absolute;
    margin: 0;
    padding: 0;
    list-style: none;
    white-space: nowrap;
  }
  .service-list li::before {
    content: "\25B9\00A0";
    font-size: 0.8em;
  }
  .align-right { text-align: right; }

  .cleaning-heading { left: 41px; top: 88px; }
  .cleaning-list { left: 41px; top: 108px; font-size: 17px; line-height: 34.8px; }

  .green-heading { right: 612px; top: 472px; }
  .green-list { right: 612px; top: 494px; font-size: 16px; line-height: 29.8px; }

  .winter-heading { left: 606px; top: 38px; }
  .winter-list { left: 606px; top: 59px; font-size: 15px; line-height: 27.1px; }

  .clearance-heading { right: 46px; top: 220px; }
  .clearance-list { right: 46px; top: 241px; font-size: 15px; line-height: 27.4px; }

  .craft-heading { left: 606px; top: 448px; }
  .craft-list { left: 606px; top: 469px; font-size: 15px; line-height: 27.4px; }

  .photo {
    position: absolute;
    border-radius: 50%;
    border: 4px solid var(--frame);
    box-sizing: border-box;
    z-index: 2;
  }
  .photo-cleaning {
    left: 352px; top: 120px; width: 206px; height: 206px;
    background: radial-gradient(circle at 40% 45%, #f3f1ec 0%, #d9dde0 55%, #b9c2c6 100%);
  }
  .photo-winter {
    left: 962px; top: 48px; width: 164px; height: 164px;
    background: radial-gradient(circle at 55% 60%, #f2f4f6 0%, #c9cfd3 60%, #7b8387 100%);
  }
  .photo-clearance {
    left: 649px; top: 227px; width: 176px; height: 176px;
    background: radial-gradient(circle at 50% 55%, #a7b0b3 0%, #7f8a86 55%, #5e5a4f 100%);
  }
  .photo-lawn {
    left: 76px; top: 492px; width: 206px; height: 206px;
    background: radial-gradient(circle at 60% 40%, #c7c9c3 0%, #6fae3a 40%, #3f7d22 100%);
  }
  .photo-craft {
    left: 991px; top: 499px; width: 164px; height: 164px;
    background: radial-gradient(circle at 45% 45%, #e3ddd4 0%, #b9b3aa 55%, #6d6a66 100%);
  }
  .soft-shadow {
    position: absolute;
    border-radius: 50%;
    background: radial-gradient(ellipse at center, var(--shadow) 0%, rgba(20,60,60,0) 70%);
  }
  .shadow-cleaning { left: 365px; top: 358px; width: 180px; height: 44px; }
  .shadow-lawn { left: 89px; top: 732px; width: 180px; height: 44px; }
  .shadow-craft { left: 995px; top: 690px; width: 156px; height: 38px; }
</style>
</head>
<body>
<main class="sheet">
  <div class="divider"></div>

  <h1 class="overview-title">Dienstleistungsübersicht</h1>

  <h2 class="service-heading cleaning-heading">Hausreinigung:</h2>
  <ul class="service-list cleaning-list">
    <li>wöchentliche Stiegenhausreinigung</li>
    <li>Fensterreinigung</li>
    <li>Büroreinigung</li>
    <li>Wohnungsreinigung</li>
    <li>Reinigung Außenflächen</li>
    <li>Garagennassreinigung</li>
    <li>Fassadenreinigung</li>
    <li>Hochdruckreinigung</li>
    <li>Graffitientfernung</li>
    <li>diverse weitere Reinigungsarbeiten</li>
  </ul>
  <div class="soft-shadow shadow-cleaning"></div>
  <div class="photo photo-cleaning" role="img" aria-label="Reinigungskraft beim Wischen eines hellen Flurs mit Putzwagen"></div>

  <h2 class="service-heading green-heading">Grünflächenpflege:</h2>
  <ul class="service-list green-list align-right">
    <li>Rasenschnitt</li>
    <li>Rasenbewässerung</li>
    <li>Sträucherrückschnitt</li>
    <li>Baumkornenrückschitt</li>
    <li>Baumrodung</li>
    <li>Baumkronenabwurf</li>
    <li>Wurzelstockfräsung</li>
    <li>Efeubeseitigung</li>
    <li>Fertigrasenverlegung</li>
    <li>diverse weitere Grünflächenpflegearbeiten</li>
  </ul>
  <div class="soft-shadow shadow-lawn"></div>
  <div class="photo photo-lawn" role="img" aria-label="Rasenmäher auf frisch gemähtem grünem Rasen"></div>

  <h2 class="service-heading winter-heading">Winterdienst:</h2>
  <ul class="service-list winter-list">
    <li>Bereitschaftsdienst vom 01.11. bis 15.04.</li>
    <li>Schneeräumung</li>
    <li>Tauwetterkontrolle</li>
    <li>Splitt- und Salzstreuung</li>
    <li>Splittkehrung bei Trockenperioden</li>
    <li>händische als auch maschinelle Räumung</li>
  </ul>
  <div class="photo photo-winter" role="img" aria-label="Arbeiter in Warnweste räumt Schnee auf einem Gehweg am Geländer"></div>

  <h2 class="service-heading clearance-heading">Entrümpelung:</h2>
  <ul class="service-list clearance-list align-right">
    <li>Fachgerechte Abfallentsorgung</li>
    <li>Sperrmüllentsorgung</li>
    <li>Firmen- und Büroräumungen</li>
    <li>Wohnungsräumungen</li>
    <li>Verlassenschaftsräumungen</li>
    <li>Dachboden- und Kellerräumungen</li>
    <li>diverse weitere Räumungs- und Entrümpelungsarbeiten</li>
  </ul>
  <div class="photo photo-clearance" role="img" aria-label="Sperrmüll mit altem Fernseher und Möbelteilen im Freien"></div>

  <h2 class="service-heading craft-heading">Handwerker-Service:</h2>
  <ul class="service-list craft-list">
    <li>Reparatur Türen und Fenster</li>
    <li>Kleinflächen verputzen und ausmalen</li>
    <li>Reparatur und Montage Geländer und Handläufe</li>
    <li>Montage Taubennetz und Taubenspitzen</li>
    <li>Reparatur und Montage Gullys</li>
    <li>Reparatur und Montage Türschließer</li>
    <li>Instandsetzung Kaminmauerwerk und Kaminköpfe</li>
    <li>Reparatur Holz-, Keramik- und Terazzoböden</li>
    <li>Montage Kantenschutzprofile</li>
    <li>Befestigung Boden- und Sockelfliesen</li>
    <li>Reparatur gebrochene Betonstufen</li>
    <li>diverse weitere Reparaturarbeiten</li>
  </ul>
  <div class="soft-shadow shadow-craft"></div>
  <div class="photo photo-craft" role="img" aria-label="Handwerker mit Akkuschrauber und Wasserwaage bei der Montage"></div>
</main>
</body>
</html>
```